1 Page Software Marketing/Sales Flyer Slick

Copperline Dynamics manufactures several software packages that we sell. We need a 1 page sales/marketing flyer slick that we will allow people to download from our site or as physical leave behinds in meetings. This 1 page slick should be visually (graphically) pleasing while carrying our message for selling our software product.

Target Market(s)

Enterprise Business Customers

Industry/Entity Type

Voip

Requirements
Must have
• Graphical representation of some hot point features, 1 Page - See PDF Detailed Description
Nice to have
• See PDF Detailed Description

```html
<!DOCTYPE html>
<html lang="en">
<head>
<meta charset="utf-8">
<title>Copperline Dynamics – Call Visibility</title>
<link rel="stylesheet" href="https://fonts.googleapis.com/css2?family=Oswald:wght@300;500;600;700&family=Roboto+Condensed:wght@600;700&display=swap">
<style>
  :root{
    --white:#ffffff;
    --navy:#1a1a6e;
    --ink:#111111;
    --brand:#1d4f86;
    --brand-dot:#1f6aa8;
    --night-1:#0a1a33;
    --night-2:#040b1a;
    --panel:rgba(214,216,222,0.88);
    --arrow-ring:#5d8fb8;
    --arrow-core:#2b3f5a;
    --mail:#4a9fd8;
  }
  *{margin:0;padding:0;box-sizing:border-box}
  html,body{width:927px;height:1200px;overflow:hidden;background:var(--white)}
  .flyer{position:relative;width:927px;height:1200px;font-family:"Oswald",sans-serif}
  .masthead{position:absolute;left:0;top:0;width:927px;height:206px;background:var(--white)}
  .brand{position:absolute;left:164px;top:46px;display:flex;align-items:center;gap:24px}
  .brand-dot{width:133px;height:133px;border-radius:50%;background:var(--brand-dot)}
  .brand-name{font-family:"Oswald",sans-serif;font-weight:300;font-size:54px;color:var(--brand);letter-spacing:0.5px}
  .backdrop{position:absolute;left:0;top:206px;width:927px;height:994px;
    background:radial-gradient(ellipse at 60% 40%, #1a3a66 0%, var(--night-1) 45%, var(--night-2) 100%)}
  .section-title{position:absolute;left:38px;color:var(--white);font-weight:600;font-size:41px;letter-spacing:0.8px;line-height:1;text-transform:uppercase}
  .panel{position:absolute;left:73px;width:802px;background:var(--panel)}
  .panel-lead{position:absolute;color:var(--navy);font-family:"Roboto Condensed",sans-serif;font-weight:700;font-size:19px;line-height:25px;text-transform:uppercase;white-space:nowrap}
  .checklist{position:absolute;list-style:none}
  .checklist li{position:absolute;left:0;display:flex;align-items:center;white-space:nowrap;color:var(--navy);font-family:"Roboto Condensed",sans-serif;font-weight:600;font-size:15px}
  .checklist svg{width:22px;height:22px;margin-right:10px;flex:none}
  .checklist.search svg{margin-right:9px}
  .note{position:absolute;left:137px;top:302px;color:var(--ink);font-family:"Roboto Condensed",sans-serif;font-weight:700;font-size:15px;line-height:22px;white-space:nowrap}
  .illustration{position:absolute;left:30px;top:65px;width:127px;height:200px;border-radius:10px;
    background:linear-gradient(160deg,#1f3d8a 0%,#12125a 100%)}
  .icon{position:absolute}
</style>
</head>
<body>
<div class="flyer">
  <header class="masthead">
    <div class="brand">
      <span class="brand-dot"></span>
      <span class="brand-name">Copperline Dynamics</span>
    </div>
  </header>

  <div class="backdrop" role="img" aria-label="Dark blue background with a glowing network of connected points"></div>

  <h2 class="section-title" style="top:244px">Searching for a call</h2>
  <section class="panel" style="top:292px;height:375px">
    <div class="illustration" role="img" aria-label="Illustration of a phone handset with a magnifying glass"></div>
    <p class="panel-lead" style="left:131px;top:12px">Search for a specific number or group of numbers<br>by department and/or by a data range</p>
    <ul class="checklist search" style="left:189px;top:74px">
      <li style="top:0"><svg viewBox="0 0 24 24"><circle cx="12" cy="12" r="11" fill="var(--arrow-ring)"/><circle cx="12" cy="12" r="8" fill="var(--arrow-core)"/><path d="M7 12h8M12 8l4 4-4 4" stroke="#9cc4e4" stroke-width="2" fill="none"/></svg>Who made this call ?</li>
      <li style="top:40px"><svg viewBox="0 0 24 24"><circle cx="12" cy="12" r="11" fill="var(--arrow-ring)"/><circle cx="12" cy="12" r="8" fill="var(--arrow-core)"/><path d="M7 12h8M12 8l4 4-4 4" stroke="#9cc4e4" stroke-width="2" fill="none"/></svg>Who received this call ?</li>
      <li style="top:81px"><svg viewBox="0 0 24 24"><circle cx="12" cy="12" r="11" fill="var(--arrow-ring)"/><circle cx="12" cy="12" r="8" fill="var(--arrow-core)"/><path d="M7 12h8M12 8l4 4-4 4" stroke="#9cc4e4" stroke-width="2" fill="none"/></svg>Why was this call disconnected ?</li>
      <li style="top:120px"><svg viewBox="0 0 24 24"><circle cx="12" cy="12" r="11" fill="var(--arrow-ring)"/><circle cx="12" cy="12" r="8" fill="var(--arrow-core)"/><path d="M7 12h8M12 8l4 4-4 4" stroke="#9cc4e4" stroke-width="2" fill="none"/></svg>What are my jitter/latency statistics for a call ?</li>
      <li style="top:159px"><svg viewBox="0 0 24 24"><circle cx="12" cy="12" r="11" fill="var(--arrow-ring)"/><circle cx="12" cy="12" r="8" fill="var(--arrow-core)"/><path d="M7 12h8M12 8l4 4-4 4" stroke="#9cc4e4" stroke-width="2" fill="none"/></svg>Does packet loss exceed my minimum threshold ?</li>
      <li style="top:199px"><svg viewBox="0 0 24 24"><circle cx="12" cy="12" r="11" fill="var(--arrow-ring)"/><circle cx="12" cy="12" r="8" fill="var(--arrow-core)"/><path d="M7 12h8M12 8l4 4-4 4" stroke="#9cc4e4" stroke-width="2" fill="none"/></svg>See statistics for a selected time range</li>
    </ul>
    <p class="note">The ability to define a group of related numbers by Department.<br>This allows for call reporting on small non-contact center groups or hunt-groups.<br>Drill down into an individual CDR entry by day or by hour.</p>
  </section>

  <h2 class="section-title" style="top:716px">Emergency number notifications</h2>
  <section class="panel" style="top:767px;height:85px">
    <svg class="icon" style="left:24px;top:-6px" width="90" height="84" viewBox="0 0 90 84" aria-hidden="true">
      <path d="M6 0h78a6 6 0 0 1 6 6v60a6 6 0 0 1-6 6H30l-14 12 2-12H6a6 6 0 0 1-6-6V6a6 6 0 0 1 6-6z" fill="var(--mail)"/>
      <path d="M22 32l23-16 23 16v24H22z" fill="#16357a"/>
      <rect x="29" y="20" width="32" height="24" fill="#ffffff"/>
      <path d="M30 26h30M30 31h30M30 36h24" stroke="#9bb" stroke-width="1.5"/>
      <path d="M22 32l23 16 23-16v24H22z" fill="#1f4aa0"/>
    </svg>
    <p class="panel-lead" style="left:135px;top:17px;font-size:20px;line-height:25px">Receive email alerts when 911 or other<br>designated emergency numbers are dialed</p>
  </section>

  <h2 class="section-title" style="top:895px">Call diagnostics feature for CMR</h2>
  <section class="panel" style="top:945px;height:133px">
    <svg class="icon" style="left:22px;top:12px" width="100" height="100" viewBox="0 0 100 100" aria-hidden="true">
      <circle cx="50" cy="50" r="49" fill="#16164f"/>
      <path d="M38 68h24l-4-6v-16a8 8 0 0 0-16 0v16z" fill="#ffffff"/>
      <circle cx="50" cy="72" r="4" fill="#ffffff"/>
      <circle cx="50" cy="36" r="3" fill="#ffffff"/>
      <path d="M30 44q-5 10 0 20M24 40q-8 14 0 28M70 44q5 10 0 20M76 40q8 14 0 28" stroke="#ffffff" stroke-width="3" fill="none"/>
    </svg>
    <p class="panel-lead" style="left:135px;top:13px;font-size:17.5px">Threshold based automatic alerting for voice and video calls:</p>
    <ul class="checklist" style="left:155px;top:44px">
      <li style="top:0"><svg viewBox="0 0 24 24"><circle cx="12" cy="12" r="11" fill="var(--arrow-ring)"/><circle cx="12" cy="12" r="8" fill="var(--arrow-core)"/><path d="M7 12h8M12 8l4 4-4 4" stroke="#9cc4e4" stroke-width="2" fill="none"/></svg>Automatic alerts for calls with high packet loss</li>
      <li style="top:30px"><svg viewBox="0 0 24 24"><circle cx="12" cy="12" r="11" fill="var(--arrow-ring)"/><circle cx="12" cy="12" r="8" fill="var(--arrow-core)"/><path d="M7 12h8M12 8l4 4-4 4" stroke="#9cc4e4" stroke-width="2" fill="none"/></svg>Automatic alerts for calls with high latency</li>
      <li style="top:59px"><svg viewBox="0 0 24 24"><circle cx="12" cy="12" r="11" fill="var(--arrow-ring)"/><circle cx="12" cy="12" r="8" fill="var(--arrow-core)"/><path d="M7 12h8M12 8l4 4-4 4" stroke="#9cc4e4" stroke-width="2" fill="none"/></svg>Automatic alerts for calls with high jitter</li>
    </ul>
  </section>
</div>
</body>
</html>
```